Business Card Design Project

Looking for a simple and stylish business card. We are an Advertising Company. The card Must feature the company logo (attached) and also this info.
p: 0481629054
e: sales@rv-promo.com.au
w: www.rv-promo.com.au
We Advertise mainly using TV screens featured in restaurants and cafe. See website for more about the business.
Not really looking for a plain background, but at the same time do not want to much happening in the Background. I am not really to fussy though with the design or the colour scheme, and I am leaving the creativity part up to you creative designers.

```html
<!DOCTYPE html>
<html lang="en">
<head>
<meta charset="utf-8">
<title>RV Promo – Business Card</title>
<link rel="stylesheet" href="https://fonts.googleapis.com/css2?family=Open+Sans:wght@400;600;700&display=swap">
<style>
  :root {
    --backdrop: #e8e3dc;
    --card-white: #ffffff;
    --card-shade: #e4e4e4;
    --brand-blue: #1a4a9a;
    --brand-blue-light: #2a5fb0;
    --brand-pink: #e0205e;
    --ink-dark: #555555;
    --ink-contact: #4a4a4a;
  }
  * { margin: 0; padding: 0; box-sizing: border-box; }
  html, body {
    width: 1200px;
    height: 1200px;
    overflow: hidden;
  }
  body {
    background: var(--backdrop);
    font-family: "Open Sans", Arial, sans-serif;
    position: relative;
  }
  .card {
    position: absolute;
    left: 200px;
    width: 800px;
    height: 457px;
    box-shadow: 0 10px 30px rgba(0,0,0,0.18);
    overflow: hidden;
  }

  /* Front */
  .card-front {
    top: 90px;
    background: radial-gradient(ellipse at 35% 65%, var(--card-white) 40%, var(--card-shade) 100%);
  }
  .edge-stripe {
    position: absolute;
    left: 0;
    top: 0;
    width: 18px;
    height: 100%;
    background: linear-gradient(to bottom, var(--brand-blue) 0 77%, var(--brand-pink) 77% 100%);
  }
  .front-wordmark {
    position: absolute;
    left: 110px;
    top: 250px;
    font-size: 58px;
    font-weight: 400;
    letter-spacing: 2px;
    color: var(--brand-blue);
  }
  .holder {
    position: absolute;
    left: 470px;
    top: 78px;
    text-align: center;
    color: var(--ink-dark);
  }
  .holder-name {
    font-size: 36px;
    font-weight: 700;
    line-height: 1.1;
  }
  .holder-role {
    font-size: 16px;
    letter-spacing: 5px;
    margin-top: 2px;
  }
  .contact-list {
    position: absolute;
    left: 520px;
    top: 235px;
    list-style: none;
    color: var(--ink-contact);
    font-size: 17px;
    line-height: 38px;
  }
  .contact-list .label { font-weight: 600; }

  /* Back */
  .card-back {
    top: 650px;
    background: radial-gradient(ellipse at 85% 10%, var(--brand-blue-light) 0%, var(--brand-blue) 55%, #163f88 100%);
  }
  .back-wordmark {
    position: absolute;
    left: 0;
    right: 0;
    top: 155px;
    text-align: center;
    font-size: 120px;
    font-weight: 400;
    letter-spacing: 6px;
    color: var(--card-white);
    line-height: 1;
  }
</style>
</head>
<body>
  <section class="card card-front">
    <div class="edge-stripe"></div>
    <div class="front-wordmark">RV PROMO</div>
    <div class="holder">
      <div class="holder-name">Daniel Hart</div>
      <div class="holder-role">CEO</div>
    </div>
    <ul class="contact-list">
      <li><span class="label">p :</span> 0481629054</li>
      <li><span class="label">e :</span> sales@rv-promo.com.au</li>
      <li><span class="label">w:</span> www.rv-promo.com.au</li>
    </ul>
  </section>

  <section class="card card-back">
    <div class="back-wordmark">RV PROMO</div>
  </section>
</body>
</html>
```